Logo & Responsive Website Design for Mortgage Company

Talvo Mortgage is a new Mortgage Fin-Tech company that will use its own innovative, proprietary technology for lead generation, mortgage origination, and processing of residential home loans in the US. The design should convey that we are a technology-driven company, offering borrowers seeking home loans an exceptional experience throughout the borrowing process.

We are looking for designs that are elegant, convey technical competency, simple to navigate, and set us apart from the competition.

We are not set on any particular colors at this point, so feel free to choose the best colors for your particular designs.

Please include both desktop and mobile designs.

Some Examples of Mortgage Websites. These are to show the typical content, not designs that we particularly like or dislike.
https://www.pondrel.example/
https://www.kmtfunding.example/
https://dulvamortgage.example/
https://wexo.example/
https://primecoastlending.example/

Please send comments with additional questions.

Thank You For your participation.

Target Market(s)

U.S. Residential Home Loan Seekers

Industry/Entity Type

FinTech Mortgage

Number of Pages Required

2 page

```html
<!DOCTYPE html>
<html lang="en">
<head>
<meta charset="utf-8">
<title>Talvo Mortgage – Home</title>
<link href="https://fonts.googleapis.com/css2?family=IBM+Plex+Sans:ital,wght@0,300;0,400;0,500;0,600;0,700;1,400&display=swap" rel="stylesheet">
<style>
:root{
  --orange:#ff7b0a;
  --navy:#27215f;
  --blue:#36adf5;
  --slate:#4a5165;
  --light:#f1f1f3;
  --ink:#333843;
  --muted:#5b6070;
  --white:#fff;
}
*{box-sizing:border-box;margin:0;padding:0}
html,body{width:1200px;height:3639px;overflow:hidden}
body{font-family:"IBM Plex Sans",sans-serif;color:var(--ink);background:var(--white);position:relative}
section,header,footer{position:absolute;left:0;width:1200px}
.abs{position:absolute}
.btn{position:absolute;display:flex;align-items:center;justify-content:center;font-size:11px;font-weight:600;color:var(--white);border-radius:2px}
.btn-orange{background:var(--orange)}
.btn-blue{background:var(--blue)}
.btn-outline{border:1.5px solid var(--blue);color:var(--blue);background:var(--white)}
.section-title{position:absolute;left:0;width:1200px;text-align:center;font-size:30px;font-weight:300;color:var(--ink)}
.section-title b{font-weight:600}

/* header */
.site-header{top:0;height:94px;background:var(--white)}
.brand{position:absolute;display:flex;align-items:center;gap:8px}
.brand-mark{width:16px;height:16px;background:var(--navy)}
.brand-name{font-size:20px;font-weight:600;color:var(--navy);white-space:nowrap}
.main-nav{position:absolute;left:286px;top:39px;display:flex;gap:26px;font-size:10.5px;color:#444}
.main-nav .active{color:var(--orange)}
.main-nav .signin{color:var(--blue)}

/* hero */
.hero{top:94px;height:375px}
.hero-photo{position:absolute;inset:0;background:linear-gradient(180deg,#3b4550 0%,#5b5f5a 45%,#2d4b3b 70%,#1d3a52 100%)}
.hero h1{position:absolute;top:108px;width:1200px;text-align:center;font-size:36px;font-weight:400;color:var(--white)}
.hero h1 b{font-weight:600}
.hero p{position:absolute;top:158px;width:1200px;text-align:center;font-size:14px;color:var(--white)}

/* what we do */
.what{top:469px;height:487px}
.card{position:absolute;top:117px;width:181px}
.card-photo{height:111px;background:linear-gradient(135deg,#e9e4dc,#b9b2a7)}
.card h3{margin-top:14px;font-size:13px;font-weight:500;color:var(--ink)}
.card p{margin-top:12px;font-size:9px;line-height:15px;color:var(--muted)}

/* why */
.why{top:956px;height:331px;background:var(--light)}
.feature{position:absolute;top:113px;width:220px;text-align:center}
.feature h3{margin-top:14px;font-size:13px;font-weight:600;color:var(--navy)}
.feature p{margin-top:12px;font-size:9px;line-height:15px;color:var(--muted)}

/* story */
.story{top:1287px;height:312px;background:var(--navy)}
.story h2{position:absolute;left:613px;top:60px;font-size:28px;font-weight:300;color:var(--white);line-height:37px}
.story h2 b{font-weight:600}
.story p{position:absolute;left:613px;top:150px;width:420px;font-size:12px;line-height:19px;color:#e6e4f2;white-space:nowrap}

/* how */
.how{top:1599px;height:401px}
.step{position:absolute;top:112px;width:240px;text-align:center}
.step-circle{position:relative;margin:0 auto;width:88px;height:88px;border-radius:50%;border:1.5px solid var(--navy);display:flex;align-items:center;justify-content:center}
.step-num{position:absolute;bottom:-8px;left:36px;width:16px;height:16px;border-radius:50%;background:var(--blue);color:var(--white);font-size:9px;display:flex;align-items:center;justify-content:center}
.step h3{margin-top:18px;font-size:13px;font-weight:600;color:var(--navy)}
.step p{margin-top:2px;font-size:12.5px;line-height:19px;color:var(--muted)}

/* testimonials */
.testimonials{top:2000px;height:425px;background:var(--slate)}
.testimonials .section-title{color:var(--white)}
.quote-badge{position:absolute;left:565px;top:121px;width:70px;height:70px;border-radius:50%;border:1.5px solid var(--blue);display:flex;align-items:center;justify-content:center}
.quote-badge span{width:54px;height:54px;border-radius:50%;background:var(--blue);color:var(--white);font-size:30px;font-weight:700;display:flex;align-items:center;justify-content:center;line-height:1}
.quote-text{position:absolute;left:250px;top:196px;width:700px;text-align:center;font-size:12.5px;line-height:19px;font-style:italic;color:#eef0f5;white-space:nowrap}
.quote-author{position:absolute;top:288px;width:1200px;text-align:center;font-size:12.5px;font-weight:600;color:var(--white)}

/* partners */
.partners{top:2425px;height:306px;background:var(--blue)}
.partners .section-title{color:var(--white)}
.partner{position:absolute;top:122px;width:150px;height:80px;background:var(--white);display:flex;align-items:center;justify-content:center;gap:7px;font-size:15px;font-weight:600;color:var(--navy)}
.partner i{width:12px;height:12px;background:var(--orange);display:block}
.dot{position:absolute;top:233px;width:10px;height:10px;border-radius:50%;border:1.5px solid var(--white)}
.dot.on{background:var(--white);box-shadow:inset 0 0 0 2px var(--blue)}

/* faq */
.faq{top:2731px;height:525px}
.faq-list{position:absolute;left:293px;top:120px;width:614px}
.faq-item{height:38px;border-bottom:1px solid #e3e3e8;display:flex;align-items:center;justify-content:space-between;padding:0 12px;font-size:11.5px;color:var(--ink)}
.faq-item i{width:13px;height:13px;border-radius:50%;background:var(--orange);color:var(--white);font-style:normal;font-size:11px;display:flex;align-items:center;justify-content:center;line-height:1}
.faq-open{background:var(--navy);color:var(--white);padding:13px 12px 12px}
.faq-open .q{display:flex;justify-content:space-between;font-size:11.5px}
.faq-open .q i{width:13px;height:13px;border-radius:50%;background:var(--blue);color:var(--white);font-style:normal;font-size:11px;display:flex;align-items:center;justify-content:center}
.faq-open p{margin-top:10px;font-size:8.5px;line-height:13px;color:#e2e0f0}

/* footer */
.site-footer{top:3256px;height:383px;background:var(--slate);color:var(--white)}
.footer-col{position:absolute;top:70px}
.footer-col h4{font-size:14px;font-weight:500;margin-bottom:20px}
.contact-row{display:flex;gap:10px;font-size:10px;line-height:14px;margin-bottom:14px}
.contact-row.big{font-size:13px}
.quick-links a{display:block;color:var(--white);text-decoration:none;font-size:9.5px;line-height:19px}
.subscribe p{font-size:9.5px;line-height:14px;width:200px}
.email-field{margin-top:10px;width:250px;height:30px;background:var(--white);color:#777;font-size:9px;padding:0 12px;display:flex;align-items:center}
.social{position:absolute;top:312px;width:28px;height:28px;border-radius:50%}
.badge{position:absolute;top:307px;background:#e8eaf0;border-radius:3px}
.copyright{position:absolute;left:200px;top:321px;font-size:9.5px}
.copyright span{color:var(--blue)}
</style>
</head>
<body>

<header class="site-header">
  <div class="brand" style="left:108px;top:36px">
    <span class="brand-mark"></span><span class="brand-name">Talvo Mortgage</span>
  </div>
  <nav class="main-nav">
    <span class="active">Home</span><span>What We Do?</span><span>Why Choose?</span><span>How It work</span><span>Partner</span><span>Calculator</span><span>Review</span><span>FAQs</span><span>Contact Us</span><span class="signin">&#9679; Sign In</span>
  </nav>
  <div class="btn btn-orange" style="left:1006px;top:31px;width:88px;height:31px">Get started</div>
</header>

<section class="hero">
  <div class="hero-photo" role="img" aria-label="Large modern home with pool at dusk"></div>
  <h1>Get a <b>Great Mortgage Rate</b></h1>
  <p>Use one of our quick &amp; easy tools to find out what you qualify for, FREE!</p>
  <div class="btn btn-blue" style="left:478px;top:198px;width:119px;height:36px">I'm Purchasing</div>
  <div class="btn btn-orange" style="left:609px;top:198px;width:113px;height:36px">I'm Refinancing</div>
</section>

<section class="what">
  <h2 class="section-title" style="top:56px">What <b>We Do</b></h2>
  <div class="card" style="left:200px"><div class="card-photo" role="img" aria-label="Small model house on paperwork and calculator"></div><h3>Home Purchase Loans</h3><p>Lorem ipsum dolor sit amet,<br>consectetur adipiscing elit, sed do<br>eiusmod tempor ...</p></div>
  <div class="card" style="left:406px"><div class="card-photo" role="img" aria-label="Signing a home refinance document" style="background:linear-gradient(135deg,#f0eeec,#3a3f56)"></div><h3>Refinance Rates</h3><p>Lorem ipsum dolor sit amet,<br>consectetur adipiscing elit, sed do<br>eiusmod tempor ...</p></div>
  <div class="card" style="left:612px"><div class="card-photo" role="img" aria-label="Comparing rates on a laptop" style="background:linear-gradient(135deg,#d8d6d2,#8c8882)"></div><h3>Rate Comparisons</h3><p>Lorem ipsum dolor sit amet,<br>consectetur adipiscing elit, sed do<br>eiusmod tempor ...</p></div>
  <div class="card" style="left:818px"><div class="card-photo" role="img" aria-label="Handing over keys to a new property" style="background:linear-gradient(135deg,#c9d5db,#5f6d78)"></div><h3>Evaluate Your Property</h3><p>Lorem ipsum dolor sit amet,<br>consectetur adipiscing elit, sed do<br>eiusmod tempor ...</p></div>
  <div class="btn btn-outline" style="left:200px;top:331px;width:63px;height:25px;font-size:10px">More</div>
  <div class="btn btn-outline" style="left:406px;top:331px;width:63px;height:25px;font-size:10px">More</div>
  <div class="btn btn-outline" style="left:612px;top:331px;width:63px;height:25px;font-size:10px">More</div>
  <div class="btn btn-blue" style="left:818px;top:331px;width:63px;height:25px;font-size:10px">More</div>
  <div class="btn btn-orange" style="left:481px;top:386px;width:238px;height:38px;font-size:10px">Get a FREE Personalized Rate Quote Now!</div>
</section>

<section class="why">
  <h2 class="section-title" style="top:55px">Why <b>Choose?</b></h2>
  <div class="feature" style="left:215px">
    <svg width="72" height="66" viewBox="0 0 72 66" fill="none" stroke="#27215f" stroke-width="2.5"><polyline points="4,34 36,4 68,34"/><polyline points="12,28 12,62 24,62"/><polyline points="60,28 60,34"/><rect x="32" y="16" width="7" height="7" fill="#36adf5" stroke="none"/><rect x="28" y="38" width="24" height="22" stroke="#ff7b0a"/><line x1="28" y1="44" x2="52" y2="44" stroke="#ff7b0a"/><path d="M36 48l8 8M44 48l-8 8" stroke="#ff7b0a"/></svg>
    <h3>Close on Time</h3><p>Lorem Ipsum is simply dummy text of the<br>printing and typesetting industry. Lorem Ipsum<br>has been the industry.</p>
  </div>
  <div class="feature" style="left:490px">
    <svg width="72" height="66" viewBox="0 0 72 66" fill="none" stroke="#27215f" stroke-width="2.5"><polyline points="4,34 36,4 68,34"/><polyline points="12,28 12,62"/><polyline points="60,28 60,62"/><rect x="32" y="16" width="7" height="7" fill="#36adf5" stroke="none"/><path d="M30 60l14-22" stroke="#ff7b0a"/><circle cx="31" cy="42" r="3" stroke="#ff7b0a"/><circle cx="43" cy="56" r="3" stroke="#ff7b0a"/></svg>
    <h3>Low Rates &amp; Fees</h3><p>Lorem Ipsum is simply dummy text of the<br>printing and typesetting industry. Lorem Ipsum<br>has been the industry.</p>
  </div>
  <div class="feature" style="left:765px">
    <svg width="72" height="66" viewBox="0 0 72 66" fill="none" stroke="#27215f" stroke-width="2.5"><polyline points="4,34 36,4 68,34"/><polyline points="12,28 12,62"/><polyline points="60,28 60,62"/><rect x="32" y="16" width="7" height="7" fill="#36adf5" stroke="none"/><path d="M26 58v-8a10 10 0 0 1 20 0v8" stroke="#ff7b0a"/><rect x="24" y="52" width="5" height="8" stroke="#ff7b0a"/><rect x="43" y="52" width="5" height="8" stroke="#ff7b0a"/></svg>
    <h3>Customer Service</h3><p>Lorem Ipsum is simply dummy text of the<br>printing and typesetting industry. Lorem Ipsum<br>has been the industry.</p>
  </div>
</section>

<section class="story">
  <svg class="abs" style="left:0;top:0" width="640" height="312" viewBox="0 0 640 312">
    <path d="M0 0H390C520 60 600 140 560 220L505 312H0Z" fill="url(#villa)" role="img" aria-label="White beachfront villa with pool"/>
    <path d="M390 0H418C560 68 622 150 576 226L518 312H505L560 220C600 140 520 60 390 0Z" fill="#ff7b0a"/>
    <defs><linearGradient id="villa" x1="0" y1="0" x2="0" y2="1"><stop offset="0" stop-color="#bcd8ea"/><stop offset=".55" stop-color="#e3e7ea"/><stop offset="1" stop-color="#5aa8c8"/></linearGradient></defs>
  </svg>
  <h2>You've Got a Story, <b>We've<br>Got a Mortgage.</b></h2>
  <p>Lorem Ipsum is simply dummy text of the printing and typese<br>tting industry lorem Ipsum has been the industry's.</p>
  <div class="btn btn-blue" style="left:613px;top:210px;width:137px;height:35px;font-size:10px">Use Our Calculators</div>
</section>

<section class="how">
  <h2 class="section-title" style="top:56px">How it <b>Works</b></h2>
  <div class="step" style="left:205px">
    <div class="step-circle"><svg width="32" height="32" viewBox="0 0 32 32" fill="none" stroke="#ff7b0a" stroke-width="2"><path d="M8 5l5 6-3 3c2 4 5 7 9 9l3-3 6 5-3 4C15 28 4 17 5 8z"/><path d="M18 6a8 8 0 0 1 8 8M18 11a3 3 0 0 1 3 3"/></svg><span class="step-num">1</span></div>
    <h3>Inquire Now</h3><p>lorem Ipsum is simply dummy text of<br>industry dummy.</p>
  </div>
  <div class="step" style="left:480px">
    <div class="step-circle"><svg width="32" height="32" viewBox="0 0 32 32" fill="none" stroke="#ff7b0a" stroke-width="2"><rect x="4" y="6" width="24" height="22"/><line x1="4" y1="12" x2="28" y2="12"/><line x1="10" y1="3" x2="10" y2="8"/><line x1="22" y1="3" x2="22" y2="8"/><path d="M9 17h3M15 17h3M21 17h3M9 22h3M15 22h3M21 22h3"/></svg><span class="step-num">2</span></div>
    <h3>Learn About Your Options</h3><p>lorem Ipsum is simply dummy text of<br>industry dummy.</p>
  </div>
  <div class="step" style="left:755px">
    <div class="step-circle"><svg width="32" height="32" viewBox="0 0 32 32" fill="none" stroke="#ff7b0a" stroke-width="2"><rect x="6" y="5" width="20" height="24"/><rect x="12" y="3" width="8" height="4"/><path d="M10 13h2M15 13h7M10 18h2M15 18h7M10 23h2M15 23h7"/></svg><span class="step-num">3</span></div>
    <h3>Get Approved and Close</h3><p>lorem Ipsum is simply dummy text of<br>industry dummy.</p>
  </div>
  <div class="btn btn-orange" style="left:543px;top:301px;width:112px;height:38px;font-size:10px">Get started</div>
</section>

<section class="testimonials">
  <h2 class="section-title" style="top:55px">Happy <b>Clients Say</b></h2>
  <div class="quote-badge"><span>&ldquo;</span></div>
  <svg class="abs" style="left:198px;top:228px" width="14" height="20" viewBox="0 0 14 20" fill="none" stroke="#c9ccd6" stroke-width="1.5"><path d="M11 1L2 10l9 9"/></svg>
  <svg class="abs" style="left:988px;top:228px" width="14" height="20" viewBox="0 0 14 20" fill="none" stroke="#ff7b0a" stroke-width="1.5"><path d="M3 1l9 9-9 9"/></svg>
  <p class="quote-text">&ldquo; It is a long established fact that a reader will be distracted by the readable content<br>of a page when looking at its layout. The point of using Lorem Ipsum is that it has a more-or-less normal<br>distribution of letters, as opposed to using 'Content here, content here', making it look like<br>readable English Many desktop. &rdquo;</p>
  <div class="quote-author">Standard Chunk</div>
  <div class="btn btn-orange" style="left:550px;top:333px;width:100px;height:35px;font-size:10px">View All</div>
</section>

<section class="partners">
  <h2 class="section-title" style="top:60px">Our <b>Partners</b></h2>
  <div class="partner" style="left:200px"><i></i>Northgate</div>
  <div class="partner" style="left:362px"><i></i>Brightline</div>
  <div class="partner" style="left:525px"><i></i>Selvane</div>
  <div class="partner" style="left:687px"><i></i>Corvix</div>
  <div class="partner" style="left:850px"><i></i>Covantra</div>
  <span class="dot" style="left:563px"></span><span class="dot on" style="left:584px"></span><span class="dot" style="left:605px"></span><span class="dot" style="left:626px"></span>
</section>

<section class="faq">
  <h2 class="section-title" style="top:56px">Frequently <b>Asked Questions</b></h2>
  <div class="faq-list">
    <div class="faq-item">Contrary to Popular Belief, Lorem Ipsum is Not Simply?<i>+</i></div>
    <div class="faq-open"><div class="q">There are many variations of passages?<i>&minus;</i></div><p>But I must explain to you how all this mistaken idea of denouncing pleasure and praising pain was born and I will give<br>you a complete account of the system, and expound the actual teachings of the great explorer of the truth, the master-builder<br>of human happiness.</p></div>
    <div class="faq-item">Lorem Ipsum is Simply Dummy Text?<i>+</i></div>
    <div class="faq-item">It is a Long Established Fact That a Reader Will?<i>+</i></div>
    <div class="faq-item">There Are Many Variations of Passages?<i>+</i></div>
    <div class="faq-item">On the Other Hand, We Denounce with Righteous?<i>+</i></div>
  </div>
  <div class="btn btn-blue" style="left:550px;top:426px;width:100px;height:37px;font-size:10px">Contact Us</div>
</section>

<footer class="site-footer">
  <div class="brand" style="left:200px;top:100px">
    <span class="brand-mark" style="background:var(--orange)"></span><span class="brand-name" style="color:var(--white);font-size:22px">Talvo Mortgage</span>
  </div>
  <div class="footer-col" style="left:406px">
    <h4>Contact Us</h4>
    <div class="contact-row big"><svg width="11" height="11" viewBox="0 0 11 11" fill="#ff7b0a"><path d="M2 0l2.5 3-1.3 1.5c.8 1.5 1.8 2.5 3.3 3.3L8 6.5 11 9 9.5 11C4.5 10.5.5 6.5 0 1.5z"/></svg>555-014-2290</div>
    <div class="contact-row"><svg width="11" height="9" viewBox="0 0 11 9" fill="#36adf5"><rect width="11" height="9" rx="1"/></svg>info@talvomortgage.example</div>
    <div class="contact-row"><svg width="9" height="12" viewBox="0 0 9 12" fill="#36adf5"><path d="M4.5 0A4.5 4.5 0 0 0 0 4.5C0 8 4.5 12 4.5 12S9 8 9 4.5A4.5 4.5 0 0 0 4.5 0z"/></svg><span>Suite 4, 220 Harbor Row<br>Elmfield Park<br>Northvale 2048</span></div>
  </div>
  <div class="footer-col quick-links" style="left:612px">
    <h4>Quick Links</h4>
    <a>Home</a><a>What We Do?</a><a>Why Choose?</a><a>How It work</a><a>Partner</a><a>Calculator</a><a>Review</a><a>FAQs</a><a>Contact Us</a>
  </div>
  <div class="footer-col subscribe" style="left:750px">
    <h4>Subscribe to Keep Up to Date</h4>
    <p>Get Updated with Latest Offers on<br>Home Loans!</p>
    <div class="email-field">Enter Email Address ...</div>
    <div class="btn btn-orange" style="left:0;top:148px;width:88px;height:29px;font-size:10px">Send</div>
  </div>
  <div class="copyright">&copy; 2022 <span>Talvo Mortgage</span>. All Right Reserved</div>
  <span class="social" style="left:612px;background:var(--blue)"></span>
  <span class="social" style="left:651px;background:var(--orange)"></span>
  <span class="social" style="left:690px;background:var(--blue)"></span>
  <span class="badge" style="left:809px;width:34px;height:36px"></span>
  <span class="badge" style="left:862px;width:138px;height:36px;background:#1e5f9e"></span>
  <svg class="abs" style="left:1093px;top:316px" width="15" height="18" viewBox="0 0 15 18" fill="#ff7b0a"><path d="M7.5 0L15 18 7.5 13 0 18z"/></svg>
</footer>

</body>
</html>
```